Singapore Restaurant Menu Design

We need a menu designed for our new Singapore inspire restaurant located here in New Plymouth New Zealand. More Information in attached documents.
Updates

Sick

Target Market(s)

New Zealanders

Colors

Designer to choose only greyscale colors for use in the design.

Requirements
Nice to have
• Images of Singapore food however we do not want this to distract from the overall menu design as we still want the menu to be super clean

```html
<!DOCTYPE html>
<html lang="en">
<head>
<meta charset="utf-8">
<title>Kallang Menu</title>
<link href="https://fonts.googleapis.com/css2?family=Josefin+Sans:wght@300;400&family=Arimo:ital,wght@0,400;0,700;1,400&display=swap" rel="stylesheet">
<style>
:root{
  --stage:#ededed;
  --ink:#111111;
  --paper:#ffffff;
  --sheet:#0b0b0b;
  --leaf:#3a3a3a;
  --rule:#1a1a1a;
}
*{box-sizing:border-box;margin:0;padding:0}
html,body{width:1200px;height:1000px;overflow:hidden;background:var(--stage)}
body{position:relative;font-family:"Arimo",Arial,sans-serif;color:var(--ink)}
.page{position:absolute;top:102px;height:863px;background:var(--sheet);box-shadow:0 2px 6px rgba(0,0,0,.25)}
.page--food{left:28px;width:542px}
.page--more{left:612px;width:558px}
.page__pattern{position:absolute;inset:0;background:
  radial-gradient(ellipse at 12% 20%,var(--leaf) 0,transparent 35%),
  radial-gradient(ellipse at 90% 75%,var(--leaf) 0,transparent 35%),
  radial-gradient(ellipse at 20% 95%,var(--leaf) 0,transparent 30%),
  linear-gradient(160deg,#1c1c1c,#050505)}
.banner{position:absolute;left:40px;right:40px;top:30px;height:150px;background:var(--sheet)}
.brand{position:absolute;left:0;right:0;top:38px;text-align:center;color:var(--paper);font-family:"Josefin Sans",sans-serif;font-weight:300;font-size:42px;letter-spacing:8px}
.panel{position:absolute;background:var(--paper)}
.page--food .panel{left:40px;top:179px;width:476px;height:557px}
.page--more .panel{left:40px;top:170px;width:478px;height:534px}
.col{position:absolute;border-left:1.5px solid var(--rule);padding-left:8px;display:flex;flex-direction:column;justify-content:space-between}
.heading{font-family:"Josefin Sans",sans-serif;font-size:17px;font-weight:400;letter-spacing:.5px;margin:-6px 0 4px}
.item__row{display:flex;justify-content:space-between;font-weight:700;font-size:9.5px;line-height:1.2}
.item__price{padding-left:6px;white-space:nowrap}
.item__desc{font-style:italic;font-size:7px;line-height:1.2;margin-top:1px}
.item__note{font-size:7px;font-weight:400;font-style:normal}
.item__list{font-size:7px;margin:3px 0 0 14px;line-height:1.35}
.seasonal{font-size:7.5px;font-weight:700;margin-top:8px}
.sharing-title{position:absolute;left:20px;right:18px;top:18px;display:flex;align-items:center;gap:14px;font-family:"Josefin Sans",sans-serif;font-size:17px}
.sharing-title::before,.sharing-title::after{content:"";flex:1;height:1.5px;background:var(--rule)}
.plain{position:absolute;display:flex;flex-direction:column;justify-content:space-between}
.web{position:absolute;left:0;right:0;top:722px;text-align:center;color:var(--paper);font-family:"Josefin Sans",sans-serif;font-size:18px;letter-spacing:3px}
</style>
</head>
<body>

<section class="page page--food">
  <div class="page__pattern" role="img" aria-label="White line-art tropical palm leaves on black"></div>
  <div class="banner"><div class="brand">KALLANG</div></div>
  <div class="panel">
    <div class="col" style="left:10px;top:14px;width:226px;height:530px">
      <h2 class="heading">STARTERS</h2>
      <div class="item"><div class="item__row"><span>Bagedil (potato patties) V ( 3 pieces</span><span class="item__price">$3</span></div><p class="item__desc">Fried Mashed potato patties with fresh cilantro, spring onions &amp; spices coated in flour and egg</p></div>
      <div class="item"><div class="item__row"><span>Tahu Telor (tofu with egg ) V</span><span class="item__price">$10</span></div><p class="item__desc">Fried spiced flour coated tofu drenched in egg, topped with satay sauce, crushed nuts &amp; fresh sprouts.</p></div>
      <div class="item"><div class="item__row"><span>Epok Epok (Curry Puffs) ( 3 pieces )</span><span class="item__price">$5</span></div><p class="item__desc">Malay style empanadas stuffed with choice of :</p><ul class="item__list"><li>Chicken curry</li><li>Fork tender beef</li><li>Curried potatoes &amp; seasonal veggies</li></ul></div>
      <div class="item"><div class="item__row"><span>Pakora V / Vegan</span><span class="item__price">$5</span></div><p class="item__desc">Chickpea, red onion and potato fritters in a mildly spiced besan (chickpea flour) batter accompanied by a sweet tangy tamarind dip</p></div>
      <div class="item"><div class="item__row"><span>Chana Vada V / Vegan ( 3 pieces )</span><span class="item__price">$5</span></div><p class="item__desc">Crunchy lentil fritters with onions, spices &amp; curry leaf</p></div>
      <div class="item"><div class="item__row"><span>Fried Wonton ( 8 pieces )</span><span class="item__price">$10</span></div><p class="item__desc">Stuffed with choice of marinated spiced chicken / pork / pickled veggies with sweet soy dip</p></div>
      <div class="item"><div class="item__row"><span>Gado Gado Salad V / <span class="item__note">*Vegan options available</span></span><span class="item__price">$12</span></div><p class="item__desc">A delicate salad of thinly sliced chinese cabbage, cucumber, beansprout, potatoes, french beans tossed in peanut dressing with boiled egg &amp; marinated prawns.</p></div>
      <div class="item"><div class="item__row"><span>Satay ( 6 sticks )</span><span class="item__price">$12</span></div><p class="item__desc">Grilled aromatic chicken / beef or tempeh (soy beans) on skewers accompanied by ketupat (rice cakes), cucumber, onions &amp; Singapore satay gravy</p></div>
      <div class="item"><div class="item__row"><span>BBQ Chicken Wings ( 5 pieces )</span><span class="item__price">$15</span></div><p class="item__desc">Singapore style soy marinated BBQ chicken wings made to order with sweet chili dip</p></div>
      <div class="item"><div class="item__row"><span>Fried Carrot Cake</span><span class="item__price">$10</span></div><p class="item__desc">Savoury steamed white radish cake stir-fry with prawns &amp; egg drizzled with sweet dark soy sauce</p></div>
    </div>

    <div class="col" style="left:248px;top:14px;width:222px;height:190px">
      <h2 class="heading">ROTI</h2>
      <div class="item"><div class="item__row"><span>– made famous in Taman Serasi Singapore</span><span class="item__price">$15</span></div><p class="item__desc">Baguette loaf grilled with a topping choice of curried chicken / spiced beef or seasonal veggies cooked with egg and drizzled with chili sauce</p></div>
      <div class="item"><div class="item__row"><span>Roti Prata ( 2 pieces )</span><span class="item__price">$10</span></div><p class="item__desc">A traditional crispy street food flat bread accompanied with choice of chicken or veg curry for dipping</p></div>
      <div class="item"><div class="item__row"><span>Roti Jala - Malay netted crepe</span><span class="item__price">$15</span></div><p class="item__desc">Flour &amp; egg based batter spiced with turmeric and cumin accompanied with choice of chicken or veg curry</p></div>
      <div class="item"><div class="item__row"><span>Murtabak - stuffed prata</span><span class="item__price">$15</span></div><p class="item__desc">Flour based crispy flat bread stuffed with choice of double cooked chicken curry, sauteed beef or seasonal veg curry</p></div>
    </div>

    <div class="col" style="left:248px;top:240px;width:222px;height:304px">
      <h2 class="heading">NOODLES</h2>
      <div class="item"><div class="item__row"><span>Noodles</span><span class="item__price">$15</span></div><p class="item__desc">Wonton noodles tossed in sweet dark soy sauce, sesame oil topped with pickled chili, cucumber &amp; broth with choice of bbq pork, chicken or prawns &amp; fried crispy wontons</p></div>
      <div class="item"><div class="item__row"><span>Seafood mee goreng</span><span class="item__price">$18</span></div><p class="item__desc">Wok fried Malay style egg noodles in a homemade chili paste with prawns and squid topped with fried egg</p></div>
      <div class="item"><div class="item__row"><span>Veggie mee goreng V</span><span class="item__price">$15</span></div><p class="item__desc">Wok fried Malay style egg noodles in homemade chili paste with seasonal veggies &amp; tofu</p></div>
      <div class="item"><div class="item__row"><span>Char Kway Teow</span><span class="item__price">$15</span></div><p class="item__desc">Wok fried rice cake strips in sweet dark soy sauce, fish oil, chili paste with seafood topped with beansprouts</p></div>
      <div class="item"><div class="item__row"><span>Laksa Ala Katong Singapore</span><span class="item__price">$18</span></div><p class="item__desc">A Peranakan style prawn based broth noodles with prawns, squid and mussels topped with boiled egg &amp; fried tofu cubes</p></div>
      <div class="item"><div class="item__row"><span>Hor Fun Noodles</span><span class="item__price">$16</span></div><p class="item__desc">Flat rice noodles stir fried with dark sweet soy sauce &amp; a choice of seafood or pork in a silky egg gravy</p></div>
    </div>
  </div>
</section>

<section class="page page--more">
  <div class="page__pattern" role="img" aria-label="White line-art tropical palm leaves on black"></div>
  <div class="banner"><div class="brand">KALLANG</div></div>
  <div class="panel">
    <h2 class="sharing-title">SHARING</h2>

    <div class="plain" style="left:18px;top:52px;width:216px;height:186px">
      <div class="item"><div class="item__row"><span>Famous Singapore Chili Crab with Mantou Bun</span></div><p class="item__desc">Whole crab cooked wok style in a homemade tamarind spiked chili paste and egg sauce accompanied with Mantou buns for mopping up the gravy</p><p class="seasonal">**Seasonal pricing**</p></div>
      <div class="item"><div class="item__row"><span>Hot Plate Tofu <span class="item__note">*Vegan options available</span></span><span class="item__price">$15</span></div><p class="item__desc">Silken tofu on egg, leeks, onions with oyster sauce</p></div>
      <div class="item"><div class="item__row"><span>BBQ seafood in banana leaves</span><span class="item__price">$18</span></div><p class="item__desc">Choice of marinated seasonal fish, prawns or stuffed squid in wrapped banana leaves</p></div>
      <div class="item"><div class="item__row"><span>Malay Rendang</span><span class="item__price">$25</span></div><p class="item__desc">Beautiful rich beef curry, slow cooked with asian spices, lemongrass and kaffir lime leaves with a touch of coconut cream</p></div>
    </div>

    <div class="plain" style="left:252px;top:52px;width:210px;height:172px">
      <div class="item"><div class="item__row"><span>Sambal Kang Kong</span><span class="item__price">$10</span></div><p class="item__desc">Wok fried Water spinach tossed in belachan paste</p></div>
      <div class="item"><div class="item__row"><span>Steamed Local Fish</span><span class="item__price">$ seasonal pricing</span></div><p class="item__desc">Freshly steamed with sesame oil, fish sauce and oyster sauce in chili, onions, ginger, leek and garlic</p></div>
      <div class="item"><div class="item__row"><span>Sweet &amp; Sour Seasonal Fish</span><span class="item__price">$ seasonal pricing</span></div><p class="item__desc">Crispy catch on a sweet and sour sauce with flash fried capsicum, onions and pineapple</p></div>
      <div class="item"><div class="item__row"><span>Seasonal veggies in oyster sauce</span><span class="item__price">$12</span></div><p class="item__note">*Vegan options available</p><p class="item__desc">Stir fried seasonal veggies tossed in sweet oyster sauce topped with fried shallot</p></div>
    </div>

    <div class="col" style="left:10px;top:272px;width:228px;height:226px">
      <h2 class="heading">RICE</h2>
      <div class="item"><div class="item__row"><span>Singapore Chicken rice (Family style sharing)</span></div><p class="item__desc">Aromatic roasted chicken with fragrant rice cooked in a chicken broth accompanied by seasonal veg in oyster sauce and ginger sweet chili dip</p><div class="item__row" style="margin-top:3px"><span>Half chicken for 2 pax</span><span class="item__price">$20</span></div><div class="item__row"><span>Whole chicken for 4 pax</span><span class="item__price">$35</span></div></div>
      <div class="item"><div class="item__row"><span>Nasi Lemak 2 pax</span><span class="item__price">$18</span></div><p class="item__desc">Jasmine rice cooked in coconut cream infused in pandan leaves, comes with condiments of fried egg, ikan bilis, toasted nuts, crispy fried chicken &amp; shrimp based sambal</p></div>
      <div class="item"><div class="item__row"><span>Fried Rice</span><span class="item__price">$18</span></div><p class="item__desc">Chinese style fried rice with choice of chicken, beef or veg in sesame oil &amp; fish sauce</p></div>
      <div class="item"><div class="item__row"><span>Black Pepper Rice</span><span class="item__price">$18</span></div><p class="item__desc">Fragrant white rice accompanied by a choice of tender beef, chicken or seafood in a black pepper sauce</p></div>
    </div>

    <div class="col" style="left:244px;top:272px;width:222px;height:222px">
      <h2 class="heading">DESSERT</h2>
      <div class="item"><div class="item__row"><span>Apam Balek</span><span class="item__price">$10</span></div><p class="item__desc">Malay style sweet pancake filled with crushed toasted nuts, caramelised onions accompanied with ice cream and caramelised condensed milk</p></div>
      <div class="item"><div class="item__row"><span>Kueh Dadar</span><span class="item__price">$10</span></div><p class="item__desc">Grated coconut cooked in gula melaka (palm sugar) and wrapped in a pandan infused crepe</p></div>
      <div class="item"><div class="item__row"><span>Sago Gula Melaka</span><span class="item__price">$10</span></div><p class="item__desc">Creamy tapioca pearl pudding served with thick caramelised palm sugar</p></div>
      <div class="item"><div class="item__row"><span>Kueh Seri Muke</span><span class="item__price">$10</span></div><p class="item__desc">Steamed layer of Glutinous rice and pandan infused coconut milk topped with toasted desiccated coconut</p></div>
    </div>
  </div>
  <p class="web">WWW.KALLANGEATS.COM</p>
</section>

</body>
</html>
```